A4 Back cover of local magazine to advertise my music school

I have a small music school. We teach all instruments and music theory. We also teach a subject called "Leaving Cert Music" which is an important one to push. Another subject I need to push is "pre Instrumental music" and I sometimes think people don't understand what that is. (For my designer: Pre instrumental music is an introduction to music for early years kids 5-8yrs before they start an actual instrument)
We have a local magazine and I have taken the back cover in full colour for a year.
I need a good ad that can last the year selling and promoting the work we do.
We also make music videos for the students and this is a great cv for us but also great for the kids. I'd like to promote the idea that this music school is a "cooler" music school to come to than all the others.
I will send photos but we are not just limited by these. If you want some different ones or some stock photo that would be better then just ask.

I'm just searching for pictures at the moment and I don't have much so for now lets look at some ideas with some stock images and see how we go from there.

Target Market(s)

Parents of music students. Typically 30-55yrs

Industry/Entity Type

Education

Font styles to use
Serif

Requirements
Must have
• My logo. Open 6 days per week. Stage payment plans. The items mentioned in the description above.
• Contact details
Nice to have
• An eye catching feel. People should be drawn to it. More graphic than words maybe????
Should not have
• It must not be an old boring ad that we see everyday. Please ....something a little creative

```html
<!DOCTYPE html>
<html lang="en">
<head>
<meta charset="utf-8">
<title>Glenmore School of Music – Back Cover Ad</title>
<link rel="stylesheet" href="https://fonts.googleapis.com/css2?family=Cinzel:wght@400;500;600&display=swap">
<style>
  :root {
    --page-bg: #ffffff;
    --cream: #f6f0de;
    --sun: #fbb934;
    --title-grey: #6e5f4c;
    --title-brown: #6b4220;
    --copy-brown: #8b5a26;
    --ink: #1c130b;
    --white: #ffffff;
  }
  * { box-sizing: border-box; margin: 0; padding: 0; }
  html, body {
    width: 1200px; height: 1200px; overflow: hidden;
    background: var(--page-bg);
  }
  .canvas { position: relative; width: 1200px; height: 1200px; }
  .ad {
    position: absolute; left: 152px; top: 20px;
    width: 1020px; height: 1320px;
    transform: scale(0.8788); transform-origin: top left;
    background: var(--sun);
    font-family: "Cinzel", serif;
    overflow: hidden;
  }
  .ad__top { position: absolute; inset: 0 0 auto 0; height: 610px; background: var(--cream); }
  .ad__tab { position: absolute; left: 450px; top: 0; width: 117px; height: 55px; background: var(--sun); }
  .headline {
    position: absolute; left: 0; right: 0; top: 72px;
    text-align: center; font-weight: 400; line-height: 1;
  }
  .headline__lead { display: block; font-size: 88px; color: var(--title-grey); letter-spacing: 1px; }
  .headline__main { display: block; font-size: 88px; color: var(--title-brown); margin-top: 2px; letter-spacing: 1px; }
  .hero {
    position: absolute; left: 80px; top: 275px; width: 870px; height: 582px;
    border: 4px solid var(--white);
    background: linear-gradient(135deg, #8a6a4a 0%, #c9b79b 30%, #e8dfcf 50%, #9a5a2e 75%, #5d4030 100%);
  }
  .hero__hours {
    position: absolute; right: 22px; bottom: 10px;
    color: var(--white); font-size: 26px; font-weight: 500;
  }
  .offer { position: absolute; top: 888px; left: 0; right: 0; height: 140px; }
  .offer__divider { position: absolute; top: 0; width: 2px; height: 140px; background: var(--white); }
  .offer__col {
    position: absolute; top: 30px; width: 300px; margin-left: -150px;
    text-align: center; color: var(--copy-brown); font-size: 19px; line-height: 29px;
  }
  .offer__col p + p { margin-top: 8px; }
  .brand {
    position: absolute; left: 0; right: 0; top: 1085px;
    display: flex; justify-content: center; align-items: center; gap: 18px;
    color: var(--ink);
  }
  .brand__dot { width: 34px; height: 34px; border-radius: 50%; background: var(--ink); }
  .brand__name { font-size: 44px; font-weight: 400; line-height: 1.05; text-align: left; }
  .brand__name span { display: block; font-size: 32px; }
  .rule { position: absolute; left: 0; height: 2px; background: var(--cream); }
  .contact-band {
    position: absolute; left: 0; right: 0; top: 1210px; height: 48px;
    background: var(--cream); display: flex; align-items: center; justify-content: center;
    color: var(--ink); font-size: 17px; letter-spacing: 0.5px;
  }
  .social { position: absolute; top: 1270px; left: 476px; display: flex; gap: 16px; }
  .social__mark { width: 22px; height: 22px; border-radius: 4px; background: var(--cream); }
</style>
</head>
<body>
<div class="canvas">
  <article class="ad">
    <div class="ad__top"></div>
    <div class="ad__tab"></div>

    <h1 class="headline">
      <span class="headline__lead">Be Part of</span>
      <span class="headline__main">Something Special</span>
    </h1>

    <div class="hero" role="img" aria-label="Photo of three children playing cello, piano and violin together in a bright music room">
      <p class="hero__hours">Open 6 days per week</p>
    </div>

    <section class="offer">
      <div class="offer__col" style="left:198px">
        <p>Music lessons<br>for all ages</p>
        <p>Music theory</p>
      </div>
      <div class="offer__divider" style="left:332px"></div>
      <div class="offer__col" style="left:497px">
        <p>Leaving Cert Music</p>
        <p style="margin-top:13px">All instruments taught<br>Singing lessons</p>
      </div>
      <div class="offer__divider" style="left:656px"></div>
      <div class="offer__col" style="left:823px">
        <p>Music preparation classes<br>for younger children</p>
        <p>Stage payment plans</p>
      </div>
    </section>

    <div class="brand">
      <div class="brand__dot"></div>
      <p class="brand__name">Glenmore<span>School of Music</span></p>
    </div>

    <div class="rule" style="top:1196px; width:1020px"></div>
    <div class="contact-band">www.glenmoreschoolofmusic.com</div>
    <div class="rule" style="top:1281px; width:465px"></div>
    <div class="rule" style="top:1281px; left:555px; width:465px"></div>
    <div class="social" aria-label="Social media links">
      <div class="social__mark"></div>
      <div class="social__mark"></div>
    </div>
  </article>
</div>
</body>
</html>
```